Gently Harbor BC 2019

Hi!
As seen from the attached, I created a 2018 BC that I really like.
It features company details on one side, and a calendar on the other side. The BC is 7" x 2" with a score, so folded it's a regular sized BC.
Company details remain the same, but I need to upgrade and refresh the calendar to 2019. Let your creative juices flow!

The submitted designs so far, while not terrible, most don't take into account that I need a refresher on the current design, but it's a BC that is double sided, and the size of a BC that's side by side wide, with score. (see the attached BC 2018 design). I need the BC to be updated with a 2019 calendar, but essentially because it's such a tiny size, to work the realistic space allocated, and make it readable and striking to stand out and very usable/practical. Let's do this people!

```html
<!DOCTYPE html>
<html lang="en">
<head>
<meta charset="utf-8">
<title>Gently Harbor – Business Card 2019</title>
<link rel="stylesheet" href="https://fonts.googleapis.com/css2?family=Open+Sans:wght@400;600;700&family=Oswald:wght@500;600&display=swap">
<style>
  :root {
    --brand-blue: #29a8e0;
    --brand-magenta: #e6157f;
    --brand-yellow: #fff200;
    --ink: #1d1d1f;
    --paper: #ffffff;
    --backdrop: #dcdcdc;
    --font-body: "Open Sans", Arial, sans-serif;
    --font-display: "Oswald", "Arial Narrow", sans-serif;
  }
  * { box-sizing: border-box; margin: 0; padding: 0; }
  html, body { width: 1200px; height: 977px; overflow: hidden; }
  body {
    background: var(--backdrop);
    font-family: var(--font-body);
    display: flex;
    align-items: center;
    justify-content: center;
    gap: 30px;
  }
  .card {
    position: relative;
    width: 560px;
    height: 320px;
    background: var(--paper);
    overflow: hidden;
    box-shadow: 0 2px 6px rgba(0,0,0,.15);
  }

  /* ---------- Calendar side ---------- */
  .calendar-panel {
    position: absolute;
    left: 0; top: 0;
    width: 438px; height: 100%;
    background: var(--brand-blue);
    color: var(--paper);
    padding: 16px 14px 0 14px;
  }
  .calendar-title {
    display: flex;
    align-items: center;
    gap: 8px;
    font-family: var(--font-display);
    font-weight: 500;
    font-size: 16px;
    letter-spacing: 1.2px;
    margin-bottom: 12px;
  }
  .calendar-title::before {
    content: "";
    width: 28px;
    height: 2px;
    background: var(--paper);
  }
  .calendar-title::after {
    content: "";
    flex: 1;
    height: 2px;
    background: var(--paper);
  }
  .year-grid {
    display: grid;
    grid-template-columns: repeat(4, 1fr);
    column-gap: 12px;
    row-gap: 8px;
  }
  .month-name {
    font-size: 7px;
    font-weight: 700;
    letter-spacing: .4px;
    margin-bottom: 2px;
    text-transform: uppercase;
  }
  .weekdays, .days {
    display: grid;
    grid-template-columns: repeat(7, 1fr);
    list-style: none;
    font-size: 6.5px;
    line-height: 8.6px;
    text-align: center;
  }
  .weekdays { font-weight: 700; font-size: 5.5px; }
  .start-2 { grid-column-start: 2; }
  .start-3 { grid-column-start: 3; }
  .start-4 { grid-column-start: 4; }
  .start-5 { grid-column-start: 5; }
  .start-6 { grid-column-start: 6; }
  .start-7 { grid-column-start: 7; }

  .brand-panel {
    position: absolute;
    right: 0; top: 0;
    width: 112px; height: 100%;
    border-left: 5px solid var(--brand-magenta);
    padding: 14px 10px 0 10px;
  }
  .brand-panel::before {
    content: "";
    position: absolute;
    left: -11px; top: 0;
    width: 6px; height: 100%;
    background: var(--paper);
  }
  .service-tags { list-style: none; display: grid; gap: 3px; }
  .service-tags li {
    font-size: 4.6px;
    font-weight: 700;
    padding: 1px 3px;
    color: var(--ink);
    white-space: nowrap;
  }
  .tag-blue { background: var(--brand-blue); }
  .tag-magenta { background: var(--brand-magenta); }
  .tag-yellow { background: var(--brand-yellow); }

  .wordmark {
    display: flex;
    align-items: center;
    gap: 6px;
    color: var(--ink);
    font-weight: 600;
  }
  .wordmark-mark { flex: none; background: var(--brand-blue); }
  .brand-panel .wordmark { margin: 30px 0 26px; font-size: 14px; line-height: 15px; }
  .brand-panel .wordmark-mark { width: 12px; height: 12px; }

  .slogan { list-style: none; display: grid; gap: 3px; justify-items: start; }
  .slogan li {
    font-family: var(--font-display);
    font-weight: 600;
    font-size: 11px;
    letter-spacing: .3px;
    padding: 1px 5px;
    line-height: 14px;
  }
  .slogan .tag-yellow { color: var(--ink); }
  .slogan .tag-magenta, .slogan .tag-blue { color: var(--paper); }

  /* ---------- Contact side ---------- */
  .contact-shapes { position: absolute; inset: 0; }
  .contact-info {
    position: absolute;
    left: 36px; top: 88px;
    color: var(--paper);
  }
  .person-name { font-size: 17px; font-weight: 700; }
  .person-role { font-size: 10px; font-weight: 600; margin-top: 2px; }
  .contact-list { list-style: none; margin-top: 34px; display: grid; gap: 4px; }
  .contact-list li {
    display: flex;
    align-items: center;
    gap: 10px;
    font-size: 11px;
  }
  .contact-list svg { width: 10px; height: 10px; flex: none; fill: var(--paper); }
  .contact-side .wordmark {
    position: absolute;
    left: 400px; top: 110px;
    font-size: 30px;
    line-height: 32px;
  }
  .contact-side .wordmark-mark { width: 20px; height: 20px; }
</style>
</head>
<body>

<section class="card calendar-side" aria-label="Calendar side">
  <div class="calendar-panel">
    <h2 class="calendar-title">FILL YOUR DAY WITH PURPOSE&nbsp;&nbsp;2019</h2>
    <div class="year-grid">
      <div class="month"><h3 class="month-name">January</h3>
        <ol class="weekdays"><li>S</li><li>M</li><li>T</li><li>W</li><li>T</li><li>F</li><li>S</li></ol>
        <ol class="days"><li class="start-3">1</li><li>2</li><li>3</li><li>4</li><li>5</li><li>6</li><li>7</li><li>8</li><li>9</li><li>10</li><li>11</li><li>12</li><li>13</li><li>14</li><li>15</li><li>16</li><li>17</li><li>18</li><li>19</li><li>20</li><li>21</li><li>22</li><li>23</li><li>24</li><li>25</li><li>26</li><li>27</li><li>28</li><li>29</li><li>30</li><li>31</li></ol></div>
      <div class="month"><h3 class="month-name">February</h3>
        <ol class="weekdays"><li>S</li><li>M</li><li>T</li><li>W</li><li>T</li><li>F</li><li>S</li></ol>
        <ol class="days"><li class="start-6">1</li><li>2</li><li>3</li><li>4</li><li>5</li><li>6</li><li>7</li><li>8</li><li>9</li><li>10</li><li>11</li><li>12</li><li>13</li><li>14</li><li>15</li><li>16</li><li>17</li><li>18</li><li>19</li><li>20</li><li>21</li><li>22</li><li>23</li><li>24</li><li>25</li><li>26</li><li>27</li><li>28</li></ol></div>
      <div class="month"><h3 class="month-name">March</h3>
        <ol class="weekdays"><li>S</li><li>M</li><li>T</li><li>W</li><li>T</li><li>F</li><li>S</li></ol>
        <ol class="days"><li class="start-6">1</li><li>2</li><li>3</li><li>4</li><li>5</li><li>6</li><li>7</li><li>8</li><li>9</li><li>10</li><li>11</li><li>12</li><li>13</li><li>14</li><li>15</li><li>16</li><li>17</li><li>18</li><li>19</li><li>20</li><li>21</li><li>22</li><li>23</li><li>24</li><li>25</li><li>26</li><li>27</li><li>28</li><li>29</li><li>30</li><li>31</li></ol></div>
      <div class="month"><h3 class="month-name">April</h3>
        <ol class="weekdays"><li>S</li><li>M</li><li>T</li><li>W</li><li>T</li><li>F</li><li>S</li></ol>
        <ol class="days"><li class="start-2">1</li><li>2</li><li>3</li><li>4</li><li>5</li><li>6</li><li>7</li><li>8</li><li>9</li><li>10</li><li>11</li><li>12</li><li>13</li><li>14</li><li>15</li><li>16</li><li>17</li><li>18</li><li>19</li><li>20</li><li>21</li><li>22</li><li>23</li><li>24</li><li>25</li><li>26</li><li>27</li><li>28</li><li>29</li><li>30</li></ol></div>
      <div class="month"><h3 class="month-name">May</h3>
        <ol class="weekdays"><li>S</li><li>M</li><li>T</li><li>W</li><li>T</li><li>F</li><li>S</li></ol>
        <ol class="days"><li class="start-4">1</li><li>2</li><li>3</li><li>4</li><li>5</li><li>6</li><li>7</li><li>8</li><li>9</li><li>10</li><li>11</li><li>12</li><li>13</li><li>14</li><li>15</li><li>16</li><li>17</li><li>18</li><li>19</li><li>20</li><li>21</li><li>22</li><li>23</li><li>24</li><li>25</li><li>26</li><li>27</li><li>28</li><li>29</li><li>30</li><li>31</li></ol></div>
      <div class="month"><h3 class="month-name">June</h3>
        <ol class="weekdays"><li>S</li><li>M</li><li>T</li><li>W</li><li>T</li><li>F</li><li>S</li></ol>
        <ol class="days"><li class="start-7">1</li><li>2</li><li>3</li><li>4</li><li>5</li><li>6</li><li>7</li><li>8</li><li>9</li><li>10</li><li>11</li><li>12</li><li>13</li><li>14</li><li>15</li><li>16</li><li>17</li><li>18</li><li>19</li><li>20</li><li>21</li><li>22</li><li>23</li><li>24</li><li>25</li><li>26</li><li>27</li><li>28</li><li>29</li><li>30</li></ol></div>
      <div class="month"><h3 class="month-name">July</h3>
        <ol class="weekdays"><li>S</li><li>M</li><li>T</li><li>W</li><li>T</li><li>F</li><li>S</li></ol>
        <ol class="days"><li class="start-2">1</li><li>2</li><li>3</li><li>4</li><li>5</li><li>6</li><li>7</li><li>8</li><li>9</li><li>10</li><li>11</li><li>12</li><li>13</li><li>14</li><li>15</li><li>16</li><li>17</li><li>18</li><li>19</li><li>20</li><li>21</li><li>22</li><li>23</li><li>24</li><li>25</li><li>26</li><li>27</li><li>28</li><li>29</li><li>30</li><li>31</li></ol></div>
      <div class="month"><h3 class="month-name">August</h3>
        <ol class="weekdays"><li>S</li><li>M</li><li>T</li><li>W</li><li>T</li><li>F</li><li>S</li></ol>
        <ol class="days"><li class="start-5">1</li><li>2</li><li>3</li><li>4</li><li>5</li><li>6</li><li>7</li><li>8</li><li>9</li><li>10</li><li>11</li><li>12</li><li>13</li><li>14</li><li>15</li><li>16</li><li>17</li><li>18</li><li>19</li><li>20</li><li>21</li><li>22</li><li>23</li><li>24</li><li>25</li><li>26</li><li>27</li><li>28</li><li>29</li><li>30</li><li>31</li></ol></div>
      <div class="month"><h3 class="month-name">September</h3>
        <ol class="weekdays"><li>S</li><li>M</li><li>T</li><li>W</li><li>T</li><li>F</li><li>S</li></ol>
        <ol class="days"><li>1</li><li>2</li><li>3</li><li>4</li><li>5</li><li>6</li><li>7</li><li>8</li><li>9</li><li>10</li><li>11</li><li>12</li><li>13</li><li>14</li><li>15</li><li>16</li><li>17</li><li>18</li><li>19</li><li>20</li><li>21</li><li>22</li><li>23</li><li>24</li><li>25</li><li>26</li><li>27</li><li>28</li><li>29</li><li>30</li></ol></div>
      <div class="month"><h3 class="month-name">October</h3>
        <ol class="weekdays"><li>S</li><li>M</li><li>T</li><li>W</li><li>T</li><li>F</li><li>S</li></ol>
        <ol class="days"><li class="start-3">1</li><li>2</li><li>3</li><li>4</li><li>5</li><li>6</li><li>7</li><li>8</li><li>9</li><li>10</li><li>11</li><li>12</li><li>13</li><li>14</li><li>15</li><li>16</li><li>17</li><li>18</li><li>19</li><li>20</li><li>21</li><li>22</li><li>23</li><li>24</li><li>25</li><li>26</li><li>27</li><li>28</li><li>29</li><li>30</li><li>31</li></ol></div>
      <div class="month"><h3 class="month-name">November</h3>
        <ol class="weekdays"><li>S</li><li>M</li><li>T</li><li>W</li><li>T</li><li>F</li><li>S</li></ol>
        <ol class="days"><li class="start-6">1</li><li>2</li><li>3</li><li>4</li><li>5</li><li>6</li><li>7</li><li>8</li><li>9</li><li>10</li><li>11</li><li>12</li><li>13</li><li>14</li><li>15</li><li>16</li><li>17</li><li>18</li><li>19</li><li>20</li><li>21</li><li>22</li><li>23</li><li>24</li><li>25</li><li>26</li><li>27</li><li>28</li><li>29</li><li>30</li></ol></div>
      <div class="month"><h3 class="month-name">December</h3>
        <ol class="weekdays"><li>S</li><li>M</li><li>T</li><li>W</li><li>T</li><li>F</li><li>S</li></ol>
        <ol class="days"><li>1</li><li>2</li><li>3</li><li>4</li><li>5</li><li>6</li><li>7</li><li>8</li><li>9</li><li>10</li><li>11</li><li>12</li><li>13</li><li>14</li><li>15</li><li>16</li><li>17</li><li>18</li><li>19</li><li>20</li><li>21</li><li>22</li><li>23</li><li>24</li><li>25</li><li>26</li><li>27</li><li>28</li><li>29</li><li>30</li><li>31</li></ol></div>
    </div>
  </div>

  <aside class="brand-panel">
    <ul class="service-tags">
      <li class="tag-blue">Toner and ink supplies</li>
      <li class="tag-magenta">Free local pickup</li>
      <li class="tag-yellow">Recycle with us today</li>
    </ul>
    <div class="wordmark"><span class="wordmark-mark"></span><span>Gently<br>Harbor</span></div>
    <ul class="slogan">
      <li class="tag-yellow">WE DO GOOD</li>
      <li class="tag-magenta">STUFF WITH</li>
      <li class="tag-blue">YOUR STUFF</li>
    </ul>
  </aside>
</section>

<section class="card contact-side" aria-label="Contact side">
  <svg class="contact-shapes" viewBox="0 0 560 320" preserveAspectRatio="none" aria-hidden="true">
    <polygon points="0,0 346,0 340,320 0,320" fill="var(--brand-blue)"/>
    <polygon points="352,0 357,0 372,320 348,320" fill="var(--brand-magenta)"/>
  </svg>

  <div class="contact-info">
    <h1 class="person-name">Daniel Reyes</h1>
    <p class="person-role">Manager</p>
    <ul class="contact-list">
      <li><svg viewBox="0 0 10 10"><path d="M2 0.5 L3.6 2.6 L2.8 3.8 Q4 6.2 6.2 7.2 L7.4 6.4 L9.5 8 L8.4 9.5 Q3.5 9 0.5 1.6 Z"/></svg>555.201.4418</li>
      <li><svg viewBox="0 0 10 10"><path d="M1 1.5 H9 V7 H4 L1.8 9 V7 H1 Z"/></svg>555.318.6632</li>
      <li><svg viewBox="0 0 10 10"><path d="M2.5 0.5 H7.5 V3 H9.5 V8.5 H0.5 V3 H2.5 Z M3.3 1.3 V3 H6.7 V1.3 Z M2 5 H8 V6 H2 Z"/></svg>555.201.4419</li>
      <li><svg viewBox="0 0 10 10"><path d="M0.5 2 H9.5 V8.5 H0.5 Z M1 2.4 L5 5.6 L9 2.4 V3.4 L5 6.6 L1 3.4 Z" fill-rule="evenodd"/></svg>pickup@gentlyharbor.com</li>
      <li><svg viewBox="0 0 10 10"><path d="M5 0.5 A4.5 4.5 0 1 0 5 9.5 A4.5 4.5 0 1 0 5 0.5 Z M5 2 A3 3 0 1 1 5 8 A3 3 0 1 1 5 2 Z" fill-rule="evenodd"/><circle cx="5" cy="5" r="1.4"/></svg>gentlyharbor.com</li>
    </ul>
  </div>

  <div class="wordmark"><span class="wordmark-mark"></span><span>Gently<br>Harbor</span></div>
</section>

</body>
</html>
```